Verdanix Medical Business Card

Create a high class Business card for Medical Aesthetics and Wellness Practice called Verdanix Medical Aesthetics and Wellness as per the logo attached.
Addresss is: 418 Harlan Brook Road Suite 312 Melville, New York 11093
Phone (555)204-7391 IG @verdanix_medical
Verdanixmedical.example

I need 5 different name configurations
1) Dr. Theo Valcourt
Aesthetics and Wellness Specialist
Medical Director

2) Rosalind Pettinger, NP
Clinical Nurse Manager

3) Marla Vostrik, RN
Aesthetic Nurse Specialist

4) Petra Halvesen, RN

5) Dana Kowbeck, L.E.
Senior Licensed Esthetician

Target Market(s)

22-55 Females

Industry/Entity Type

Medical Spa and Wellness

Contact Information for Business Card

Logo, address, phone, web, instagram, providers name

Requirements
Must have
• Attractive classy modern look

```html
<!DOCTYPE html>
<html lang="en">
<head>
<meta charset="utf-8">
<title>Verdanix Medical Business Card</title>
<link rel="stylesheet" href="https://fonts.googleapis.com/css2?family=Bodoni+Moda:wght@400&family=Cormorant+Garamond:wght@500&family=Work+Sans:wght@400;600&display=swap">
<style>
  :root {
    --backdrop: #969696;
    --card-dark: #262626;
    --card-light: #ffffff;
    --ink-light: #ffffff;
    --ink-dark: #1a1a1a;
    --ink-muted: #7a7a7a;
  }
  html, body {
    margin: 0;
    width: 1200px;
    height: 1000px;
    overflow: hidden;
    background: var(--backdrop);
  }
  .canvas {
    position: relative;
    width: 1200px;
    height: 1000px;
  }
  .card {
    position: absolute;
    width: 694px;
    height: 400px;
    border-radius: 30px;
    overflow: hidden;
  }
  .card--front {
    left: 253px;
    top: 79px;
    background: var(--card-dark);
    color: var(--ink-light);
  }
  .card--back {
    left: 259px;
    top: 523px;
    background: var(--card-light);
    color: var(--ink-dark);
  }
  .brand {
    position: absolute;
    text-align: center;
    font-family: "Cormorant Garamond", serif;
    font-weight: 500;
  }
  .brand__name {
    font-family: "Bodoni Moda", serif;
    font-weight: 400;
    letter-spacing: 3px;
    line-height: 1;
  }
  .brand__tagline {
    text-transform: uppercase;
    line-height: 1;
  }
  .brand__city {
    text-transform: uppercase;
    line-height: 1;
  }
  .card--front .brand {
    left: 35px;
    width: 360px;
    top: 170px;
  }
  .card--front .brand__name { font-size: 44px; }
  .card--front .brand__tagline { font-size: 15px; margin-top: 21px; letter-spacing: 0.3px; }
  .card--front .brand__city { font-size: 11px; margin-top: 10px; letter-spacing: 5px; }

  .card--back .brand {
    left: 0;
    width: 694px;
    top: 55px;
  }
  .card--back .brand__name { font-size: 36px; }
  .card--back .brand__tagline { font-size: 12.5px; margin-top: 14px; letter-spacing: 0.2px; }
  .card--back .brand__city { font-size: 9px; margin-top: 8px; letter-spacing: 4px; }

  .provider {
    position: absolute;
    left: 0;
    width: 694px;
    top: 178px;
    text-align: center;
    color: var(--ink-muted);
  }
  .provider__name {
    font-family: "Bodoni Moda", serif;
    font-weight: 400;
    font-size: 34px;
    letter-spacing: 0.5px;
    line-height: 1;
    text-transform: uppercase;
  }
  .provider__role {
    font-family: "Work Sans", sans-serif;
    font-size: 13px;
    letter-spacing: 2.2px;
    text-transform: uppercase;
    line-height: 24px;
  }
  .provider__name + .provider__role { margin-top: 10px; }

  .contact {
    position: absolute;
    left: 0;
    width: 694px;
    top: 316px;
    text-align: center;
    font-family: "Work Sans", sans-serif;
    font-size: 15px;
    letter-spacing: 0.9px;
    line-height: 19.5px;
    color: var(--ink-muted);
  }
  .contact strong { font-weight: 600; }
  .contact__dot {
    display: inline-block;
    width: 11px;
    height: 11px;
    border: 1.6px solid var(--ink-muted);
    border-radius: 50%;
    vertical-align: -1px;
    margin-right: 2px;
  }
</style>
</head>
<body>
<main class="canvas">
  <section class="card card--front" aria-label="Card front">
    <div class="brand">
      <div class="brand__name">Verdanix</div>
      <div class="brand__tagline">Medical Aesthetics and Wellness</div>
      <div class="brand__city">New York</div>
    </div>
  </section>

  <section class="card card--back" aria-label="Card back">
    <div class="brand">
      <div class="brand__name">Verdanix</div>
      <div class="brand__tagline">Medical Aesthetics and Wellness</div>
      <div class="brand__city">New York</div>
    </div>

    <div class="provider">
      <div class="provider__name">Dr. Theo Valcourt</div>
      <div class="provider__role">Aesthetics and Wellness Specialist</div>
      <div class="provider__role">Medical Director</div>
    </div>

    <div class="contact">
      <div>418 Harlan Brook Road Suite 312 Melville, New York 11093</div>
      <div><strong>Phone:</strong> (555) 204-7391 &bull; <span class="contact__dot"></span>@verdanix_medical</div>
      <div><strong>verdanixmedical</strong>.example</div>
    </div>
  </section>
</main>
</body>
</html>
```